Referral Portal - Mobile App Design

To create a clean easy Web App Design for a Referral portal for Customer to submit and track their referrals.

Larkmoor Energy Referral Portal

https://www.larkmoor-energy.example

We are looking for a very simple phone app that will allow users to track their referrals. The sections/ things
We need in the app are as follows:
Form to Submit new Referrals
A very visual easy to read dashboard/ graph to show total Paid vs total potential(outstanding)
Simple Visual to show total paid
List of all referrals submitted and their status
Total number of referrals submitted and what Tier they fall into and what is the next tier (how close)

The App should be a minimal clean design that the user can navigate easily without much direction given.
This app should only be designed for the mobile experience. This is meant to gamify and incentives the user
To add more referrals and get more payments. Adding something fun with the Sun would be great!

Please See Bridge file for further information. We would like to name the App Larkmoor Energy Bridge

Thank you!!

Target Market(s)

Homeowners between ages of 30-60 who are familiar with apps that they use on their phone every day

Industry/Entity Type

Solar Energy

Font styles to use
Sans Serif

Colors
fbee3e
acd136
9bcb3c
f68e4e
f37022
f78f20
ffc214
34a7d8

Requirements
Must have
• Clean simple design, easy to use design/layout of nav.
• Visual charts and big graphic $$ on how much they have in their Wallet
• Easy visual to tell apart tiers (Gold, Silver,Platinum)
Nice to have
• Fun way to incorporate a rising or glowing sun
Should not have
• Too many words, not be bright and color

```html
<!DOCTYPE html>
<html lang="en">
<head>
<meta charset="UTF-8">
<title>Larkmoor Energy Bridge – Refer Friends</title>
<link href="https://fonts.googleapis.com/css2?family=Roboto:wght@300;400;500&display=swap" rel="stylesheet">
<style>
  :root {
    --orange: #f68e4e;
    --orange-deep: #f37022;
    --sky: #6ccaf3;
    --sky-soft: #8fd6f5;
    --sun: #ffc214;
    --white: #ffffff;
    --track: #b5b5b5;
    --step-idle: #a9a9a9;
    --field-line: #c4c4c4;
    --placeholder: #b3b3b3;
    --page: #ffffff;
  }
  * { box-sizing: border-box; margin: 0; padding: 0; }
  html, body { width: 677px; height: 1200px; overflow: hidden; background: var(--page); }
  body { font-family: 'Roboto', sans-serif; }
  .screen { position: relative; width: 677px; height: 1200px; overflow: hidden; background: var(--page); }

  .status-bar {
    position: absolute; top: 0; left: 0; width: 100%; height: 34px;
    background: var(--orange); color: var(--white);
    font-size: 22px; display: flex; align-items: center; justify-content: space-between;
    padding: 0 14px;
  }
  .status-bar .signal { display: flex; gap: 4px; align-items: center; }
  .status-bar .dot { width: 10px; height: 10px; border-radius: 50%; background: var(--white); }
  .status-bar .dot.empty { background: transparent; border: 1.5px solid var(--white); }
  .status-bar .time { position: absolute; left: 50%; transform: translateX(-50%); }
  .status-bar .battery { display: flex; align-items: center; gap: 8px; }
  .battery-icon { width: 44px; height: 20px; border: 2px solid var(--white); border-radius: 3px; padding: 2px; }
  .battery-icon span { display: block; width: 55%; height: 100%; background: var(--white); }

  .app-bar {
    position: absolute; top: 34px; left: 0; width: 100%; height: 108px;
    background: var(--orange); color: var(--white);
  }
  .menu-icon { position: absolute; left: 32px; top: 40px; width: 40px; }
  .menu-icon span { display: block; height: 4px; background: var(--white); border-radius: 2px; margin-bottom: 7px; }
  .app-title { position: absolute; left: 0; right: 0; top: 38px; text-align: center; font-size: 32px; font-weight: 400; }

  .hero-art {
    position: absolute; top: 142px; left: 0; width: 677px; height: 484px;
    background: linear-gradient(170deg, var(--sky) 0%, var(--sky) 62%, var(--sky-soft) 82%, var(--sun) 100%);
  }

  .stepper { position: absolute; top: 196px; left: 80px; width: 534px; height: 44px; }
  .stepper .track { position: absolute; top: 21px; left: 20px; right: 20px; height: 4px; background: var(--track); }
  .stepper .progress { position: absolute; top: 21px; left: 20px; width: 118px; height: 4px; background: var(--orange-deep); }
  .step {
    position: absolute; top: 0; width: 44px; height: 44px; border-radius: 50%;
    background: var(--step-idle); color: var(--white); font-size: 28px;
    display: flex; align-items: center; justify-content: center;
  }
  .step.active { background: var(--orange-deep); }

  .form-heading {
    position: absolute; top: 358px; left: 0; right: 0; text-align: center;
    color: var(--white); font-size: 31px; font-weight: 500; letter-spacing: 0.5px;
  }

  .referral-form { position: absolute; top: 690px; left: 77px; width: 540px; }
  .field { display: block; height: 99px; position: relative; }
  .field input {
    position: absolute; left: 0; right: 0; top: 10px; height: 52px;
    border: none; border-bottom: 3px solid var(--field-line); background: transparent;
    font-family: 'Roboto', sans-serif; font-weight: 300; font-size: 29px; color: #555;
    padding: 0 0 6px 18px; outline: none;
  }
  .field input::placeholder { color: var(--placeholder); }

  .next-button {
    position: absolute; top: 1096px; left: 172px; width: 344px; height: 74px;
    border: none; border-radius: 37px; background: var(--orange);
    color: var(--white); font-family: 'Roboto', sans-serif; font-size: 38px; font-weight: 400;
  }
</style>
</head>
<body>
<main class="screen">
  <div class="status-bar">
    <div class="signal">
      <span class="dot"></span><span class="dot"></span><span class="dot"></span><span class="dot empty"></span><span class="dot empty"></span>
    </div>
    <span class="time">08:46 PM</span>
    <div class="battery"><span>57%</span><div class="battery-icon"><span></span></div></div>
  </div>

  <header class="app-bar">
    <div class="menu-icon"><span></span><span></span><span></span></div>
    <h1 class="app-title">Refer Friends</h1>
  </header>

  <div class="hero-art" role="img" aria-label="Illustration of a blue cloud with a yellow sun rising behind it"></div>

  <div class="stepper">
    <div class="track"></div>
    <div class="progress"></div>
    <div class="step active" style="left:0">1</div>
    <div class="step" style="left:245px">2</div>
    <div class="step" style="left:490px">3</div>
  </div>

  <h2 class="form-heading">FILL YOUR OWN INFORMATION</h2>

  <form class="referral-form">
    <label class="field"><input type="text" placeholder="FIRST NAME"></label>
    <label class="field"><input type="text" placeholder="LAST NAME"></label>
    <label class="field"><input type="email" placeholder="EMAIL"></label>
    <label class="field"><input type="tel" placeholder="PHONE"></label>
  </form>

  <button class="next-button" type="button">NEXT</button>
</main>
</body>
</html>
```